Criação de Papelaria Profissional para Crianças & Infantil
A empresa queria:
" Atraves de consultas medicas na area de pneumologia infantil para crianças e adolescentes "

```html
<!DOCTYPE html>
<html lang="pt-BR">
<head>
<meta charset="UTF-8">
<title>Envelope Saco – Dra Lúcia Prado</title>
<link rel="stylesheet" href="https://fonts.googleapis.com/css2?family=Marcellus&family=Montserrat:wght@400;600;800&display=swap">
<style>
  :root {
    --green: #7cbf3e;
    --green-dark: #6aab30;
    --teal: #4fb3b0;
    --ink: #4a4a4a;
    --paper: #ffffff;
    --board-light: #e4e4e4;
    --board-dark: #bdbdbd;
  }
  * { box-sizing: border-box; margin: 0; padding: 0; }
  html, body { width: 1200px; height: 1200px; overflow: hidden; }
  body {
    position: relative;
    background: radial-gradient(circle at 50% 45%, var(--board-light), var(--board-dark));
    font-family: "Montserrat", sans-serif;
  }
  .board-frame {
    position: absolute;
    left: 48px; top: 38px; width: 1104px; height: 1114px;
    border: 9px solid var(--paper);
    border-radius: 60px;
  }
  .board-title {
    position: absolute;
    left: 50%; top: 18px; transform: translateX(-50%);
    padding: 0 30px;
    background: #d8d8d8;
    color: var(--green);
    font-weight: 800;
    font-size: 34px;
    letter-spacing: 1px;
    line-height: 44px;
  }
  .envelope {
    position: absolute;
    top: 216px; width: 500px; height: 768px;
    box-shadow: 0 6px 18px rgba(0,0,0,.25);
    overflow: hidden;
  }
  .envelope-front { left: 96px; background: var(--green); }
  .envelope-back { left: 616px; background: var(--paper); }

  .front-rule {
    position: absolute; left: 0; right: 0; top: 730px; height: 6px;
    background: var(--paper);
  }
  .back-flap {
    position: absolute; left: 0; right: 0; top: 0; height: 84px;
    background: var(--green);
    border-radius: 0 0 44px 44px;
  }
  .back-rule {
    position: absolute; left: 0; right: 0; top: 736px; height: 6px;
    background: var(--green);
  }
  .back-base {
    position: absolute; left: 0; right: 0; top: 750px; height: 18px;
    background: var(--green);
  }

  .brand {
    position: absolute; left: 0; right: 0;
    display: flex; align-items: center; justify-content: center; gap: 12px;
    font-family: "Marcellus", serif;
    font-size: 40px;
    letter-spacing: 1px;
    white-space: nowrap;
  }
  .brand-dot { width: 16px; height: 16px; border-radius: 50%; flex: none; }
  .brand-on-green { top: 390px; color: var(--paper); }
  .brand-on-green .brand-dot { background: var(--paper); }
  .brand-on-white { top: 398px; color: var(--ink); }
  .brand-on-white .brand-dot { background: var(--green); }
  .brand-board {
    top: 1034px; left: 0; right: 0;
    color: var(--ink); font-size: 46px;
  }
  .brand-board .brand-dot { background: var(--green); width: 18px; height: 18px; }

  .contact-strip {
    position: absolute; left: 22px; right: 22px; top: 682px;
    display: flex; justify-content: space-between;
    font-size: 9px; color: #777; line-height: 15px;
  }
  .contact-col { display: flex; flex-direction: column; }
  .contact-item { display: flex; align-items: center; gap: 6px; }
  .contact-item svg { width: 10px; height: 10px; flex: none; }
</style>
</head>
<body>
  <div class="board-frame"></div>
  <div class="board-title">ENVELOPE SACO</div>

  <section class="envelope envelope-front" aria-label="Frente do envelope">
    <div class="brand brand-on-green"><span class="brand-dot"></span>Dra Lúcia Prado</div>
    <div class="front-rule"></div>
  </section>

  <section class="envelope envelope-back" aria-label="Verso do envelope">
    <div class="back-flap"></div>
    <div class="brand brand-on-white"><span class="brand-dot"></span>Dra Lúcia Prado</div>

    <div class="contact-strip">
      <div class="contact-col">
        <span class="contact-item">(11) 98765-4321
          <svg viewBox="0 0 10 10"><path d="M2 1l2 2-1 1.2c.6 1.2 1.5 2.1 2.8 2.8L7 6l2 2-1.3 1.3C4.5 9 1 5.5.7 2.3z" fill="var(--green)"/></svg></span>
        <span class="contact-item">(11) 3456-7890
          <svg viewBox="0 0 10 10"><circle cx="5" cy="5" r="4.2" fill="var(--green)"/></svg></span>
      </div>
      <div class="contact-col">
        <span class="contact-item">contato@luciaprado.com.br
          <svg viewBox="0 0 10 10"><rect x=".5" y="2" width="9" height="6" fill="var(--green)"/><path d="M.5 2l4.5 3.5L9.5 2" stroke="#fff" stroke-width=".8" fill="none"/></svg></span>
        <span class="contact-item">www.luciaprado.com.br
          <svg viewBox="0 0 10 10"><circle cx="5" cy="5" r="4.2" fill="var(--green)"/></svg></span>
      </div>
      <div class="contact-col">
        <span class="contact-item">
          <svg viewBox="0 0 10 10"><path d="M5 .5a3.3 3.3 0 0 1 3.3 3.3C8.3 6.2 5 9.5 5 9.5S1.7 6.2 1.7 3.8A3.3 3.3 0 0 1 5 .5z" fill="var(--green)"/><circle cx="5" cy="3.8" r="1.2" fill="#fff"/></svg>
          Rua das Acácias, 120 · Centro</span>
        <span class="contact-item" style="padding-left:16px">São Paulo/SP · CEP 01000-000</span>
      </div>
    </div>

    <div class="back-rule"></div>
    <div class="back-base"></div>
  </section>

  <div class="brand brand-board"><span class="brand-dot"></span>Dra Lúcia Prado</div>
</body>
</html>
```